Business Card Design for a Software Startup

We'd like to have a business card design. We already have a logo. Basically what we need is a clean design with name, address, cellphone and phone numbers, e-mail and web site address (front) and a space on the back with our logo with the company name on the right side and some texts on the bottom.
We are a development and consulting company in Brazil with highly qualified team of professionals in Java, iOS and Android development and consulting.

Target Market(s)

CIO, IT managers of mid to big size companies

Industry/Entity Type

Business

```html
<!DOCTYPE html>
<html lang="en">
<head>
<meta charset="utf-8">
<title>VORTA Business Card</title>
<link rel="stylesheet" href="https://fonts.googleapis.com/css2?family=Arimo:wght@400;700&display=swap">
<style>
  :root {
    --stage: #3b3b3b;
    --card-dark: #070a0f;
    --card-dark-glow: #163a63;
    --card-light: #f7f8f9;
    --card-light-shade: #dfe3e7;
    --brand-blue: #1f6fb8;
    --brand-navy: #143a63;
    --ink: #2b2f33;
    --ink-soft: #5a6066;
    --url-dark: #9aa6b2;
    --divider: #c9ced3;
  }
  * { box-sizing: border-box; margin: 0; padding: 0; }
  html, body { width: 893px; height: 1200px; overflow: hidden; }
  body {
    background: var(--stage);
    font-family: "Arimo", Arial, sans-serif;
    display: flex;
    flex-direction: column;
    align-items: center;
    justify-content: center;
    gap: 70px;
  }
  .card {
    position: relative;
    width: 700px;
    height: 400px;
    border-radius: 22px;
    overflow: hidden;
    box-shadow: 0 14px 30px rgba(0,0,0,0.45);
  }
  .card-texture { position: absolute; inset: 0; }

  /* Back */
  .card-back { background: var(--card-dark); }
  .card-back .card-texture {
    background: linear-gradient(115deg, var(--card-dark-glow) 0%, rgba(22,58,99,0.35) 28%, rgba(7,10,15,0) 55%);
  }
  .back-brand {
    position: absolute;
    left: 300px;
    top: 150px;
  }
  .wordmark {
    display: flex;
    align-items: center;
    gap: 14px;
    font-weight: 700;
    letter-spacing: 1px;
  }
  .wordmark-square { display: inline-block; background: var(--brand-blue); }
  .back-brand .wordmark { font-size: 82px; color: #ffffff; }
  .back-brand .wordmark-square { width: 66px; height: 66px; }
  .back-url {
    margin-top: 4px;
    margin-left: 82px;
    font-size: 14px;
    color: var(--url-dark);
  }

  /* Front */
  .card-front { background: var(--card-light); }
  .card-front .card-texture {
    background: linear-gradient(115deg, var(--card-light-shade) 0%, rgba(247,248,249,0) 40%);
  }
  .front-brand {
    position: absolute;
    left: 40px;
    top: 110px;
    width: 200px;
    display: flex;
    flex-direction: column;
    align-items: center;
  }
  .front-brand .wordmark-square { width: 100px; height: 100px; border-radius: 6px; }
  .front-brand .wordmark-name {
    margin-top: 14px;
    font-size: 44px;
    font-weight: 700;
    color: var(--brand-navy);
    letter-spacing: 1px;
  }
  .front-url { margin-top: 4px; font-size: 11px; color: var(--ink-soft); }
  .front-divider {
    position: absolute;
    left: 262px;
    top: 70px;
    width: 1px;
    height: 260px;
    background: var(--divider);
  }
  .contact {
    position: absolute;
    left: 290px;
    top: 70px;
    color: var(--ink);
  }
  .contact-name { font-size: 36px; font-weight: 400; }
  .contact-role { margin-top: 4px; font-size: 18px; color: var(--brand-blue); }
  .contact-list { list-style: none; margin-top: 28px; }
  .contact-item {
    display: flex;
    align-items: flex-start;
    gap: 12px;
    font-size: 17px;
    line-height: 1.35;
    margin-bottom: 10px;
    color: var(--ink);
  }
  .contact-icon { flex: 0 0 18px; width: 18px; height: 18px; margin-top: 2px; fill: var(--brand-blue); }
</style>
</head>
<body>

<section class="card card-back" aria-label="Card back">
  <div class="card-texture" role="img" aria-label="Dark navy background with soft blue light from the left"></div>
  <div class="back-brand">
    <div class="wordmark"><span class="wordmark-square"></span>VORTA</div>
    <p class="back-url">www.vortastudio.com</p>
  </div>
</section>

<section class="card card-front" aria-label="Card front">
  <div class="card-texture" role="img" aria-label="Light grey background with soft shading from the left"></div>
  <div class="front-brand">
    <span class="wordmark-square"></span>
    <span class="wordmark-name">VORTA</span>
    <span class="front-url">www.vortastudio.com</span>
  </div>
  <div class="front-divider"></div>
  <div class="contact">
    <h1 class="contact-name">Rafael Moretti</h1>
    <p class="contact-role">Project Owner</p>
    <ul class="contact-list">
      <li class="contact-item">
        <svg class="contact-icon" viewBox="0 0 24 24" aria-hidden="true"><path d="M12 2a7 7 0 0 0-7 7c0 5 7 13 7 13s7-8 7-13a7 7 0 0 0-7-7zm0 9.5A2.5 2.5 0 1 1 12 6.5a2.5 2.5 0 0 1 0 5z"/></svg>
        <span>Suite 410, 27 Harbor Lane<br>Porto Alegre RS 90000 Brazil</span>
      </li>
      <li class="contact-item">
        <svg class="contact-icon" viewBox="0 0 24 24" aria-hidden="true"><path d="M6.6 10.8a15 15 0 0 0 6.6 6.6l2.2-2.2a1 1 0 0 1 1-.25 11.4 11.4 0 0 0 3.6.57 1 1 0 0 1 1 1V20a1 1 0 0 1-1 1A17 17 0 0 1 3 4a1 1 0 0 1 1-1h3.5a1 1 0 0 1 1 1c0 1.25.2 2.45.57 3.57a1 1 0 0 1-.25 1z"/></svg>
        <span>+55 (0) 555 018 427</span>
      </li>
      <li class="contact-item">
        <svg class="contact-icon" viewBox="0 0 24 24" aria-hidden="true"><path d="M7 1h10a2 2 0 0 1 2 2v18a2 2 0 0 1-2 2H7a2 2 0 0 1-2-2V3a2 2 0 0 1 2-2zm0 3v14h10V4zm5 15.2a1.2 1.2 0 1 0 0 2.4 1.2 1.2 0 0 0 0-2.4z"/></svg>
        <span>+55 (51) 95550 3186</span>
      </li>
      <li class="contact-item">
        <svg class="contact-icon" viewBox="0 0 24 24" aria-hidden="true"><path d="M3 5h18a1 1 0 0 1 1 1v12a1 1 0 0 1-1 1H3a1 1 0 0 1-1-1V6a1 1 0 0 1 1-1zm9 7 8-5H4z"/></svg>
        <span>rafael@vorta.com</span>
      </li>
    </ul>
  </div>
</section>

</body>
</html>
```